a business advisory consulting website

I need a website 3-5 pages to sell my professional services in IT and Project management Consulting. My company name is Tidewell Advisory Consulting. I want it to be device friendly and easy to navigate for the busy executive however intriguing enough.
I have attached some info I drafted on About the company and personal Bio. Also there is a website that I really like that I have attached the initial site pdf and websites that I like are here: https://quillmarkfunds.example, https://lumetratrends.example, https://www.corbelteachingconsulting.example as examples. Thanks
Updates

Hi Designers, I have uploaded the logo in 3D .png format, to assist in the web design.

Target Market(s)

B2B, governments, IT companies, Project Management companies and Consulting firms, small medium enterprises to large corporate enterprises.

Industry/Entity Type

It Professional

Coding

Coded - Design and coding required

Number of Pages Required

5+ page

Font styles to use
Sans Serif

Requirements
Must have
• Home, About company, the team, what we do and contact us
Nice to have
• Blog
Should not have
• pop ups, flash

```html
<!DOCTYPE html>
<html lang="en">
<head>
<meta charset="utf-8">
<title>Tidewell Advisory Consulting — Home</title>
<link rel="stylesheet" href="https://fonts.googleapis.com/css2?family=Roboto:wght@300;400;700;900&family=Open+Sans:wght@400&display=swap">
<style>
  :root {
    --ink: #111217;
    --navy: #1f2a44;
    --accent: #e2262b;
    --nav-grey: #8c8c8c;
    --rule: #d6d6d6;
    --page: #ffffff;
    --body-text: #3a3a3a;
  }
  * { box-sizing: border-box; margin: 0; padding: 0; }
  html, body {
    width: 1200px; height: 759px; overflow: hidden;
    background: var(--page);
    font-family: "Roboto", sans-serif;
    color: var(--ink);
  }
  .page { position: relative; width: 1200px; height: 759px; overflow: hidden; }

  .site-header {
    position: absolute; left: 95px; right: 98px; top: 0; height: 94px;
    display: flex; align-items: center; justify-content: space-between;
    border-bottom: 1px solid var(--rule);
  }
  .brand { display: flex; align-items: center; gap: 10px; }
  .brand-mark { width: 14px; height: 14px; background: var(--accent); }
  .brand-name {
    font-family: "Roboto", sans-serif; font-weight: 700; font-size: 24px;
    color: var(--navy); letter-spacing: 0.2px;
  }
  .main-nav { display: flex; gap: 35px; }
  .main-nav a {
    font-family: "Roboto", sans-serif; font-weight: 400; font-size: 14px;
    text-transform: uppercase; text-decoration: none; color: var(--nav-grey);
  }
  .main-nav a.is-current { color: var(--accent); }

  .hero-visual {
    position: absolute; left: 75px; right: 0; top: 248px; height: 362px;
    background: linear-gradient(180deg, #f3f5f7 0%, #c9d0d8 25%, #8d99a7 55%, #a9b2bc 72%, #dfe3e7 86%, #eef0f2 100%);
  }
  .hero-copy { position: absolute; left: 483px; top: 203px; }
  .hero-kicker {
    font-weight: 400; font-size: 25px; letter-spacing: 4.5px;
    text-transform: uppercase; color: var(--ink);
  }
  .hero-title {
    margin-top: 10px;
    font-size: 80px; line-height: 68px; text-transform: uppercase;
    letter-spacing: -1px; color: var(--ink);
  }
  .hero-title .light { font-weight: 300; }
  .hero-title .heavy { font-weight: 900; }
  .button-read-more {
    display: inline-block; margin-top: 18px;
    width: 188px; height: 45px; line-height: 45px; text-align: center;
    background: #ffffff; color: var(--ink); text-decoration: none;
    font-weight: 700; font-size: 16px; letter-spacing: 3.5px; text-transform: uppercase;
  }

  .intro { position: absolute; left: 95px; right: 60px; top: 680px; }
  .intro-heading {
    font-weight: 700; font-size: 34px; color: var(--navy); text-transform: uppercase;
  }
  .intro-text {
    position: absolute; left: 510px; top: 32px; width: 560px;
    font-family: "Open Sans", sans-serif; font-size: 14px; line-height: 22px; color: var(--body-text);
  }
</style>
</head>
<body>
<div class="page">
  <header class="site-header">
    <div class="brand">
      <span class="brand-mark"></span>
      <span class="brand-name">Tidewell Advisory</span>
    </div>
    <nav class="main-nav">
      <a href="#" class="is-current">Home</a>
      <a href="#">About Company</a>
      <a href="#">The Team</a>
      <a href="#">What We Do</a>
      <a href="#">Blog</a>
      <a href="#">Contact Us</a>
    </nav>
  </header>

  <div class="hero-visual" role="img" aria-label="Photo of a businessman in a suit standing at a balcony railing, looking out over a city skyline of high-rise towers"></div>

  <section class="hero-copy">
    <p class="hero-kicker">Professional services in</p>
    <h1 class="hero-title">
      <span class="heavy">IT</span> <span class="light">and</span><br>
      <span class="heavy">Project</span><br>
      <span class="heavy">Management</span>
    </h1>
    <a href="#" class="button-read-more">Read More</a>
  </section>

  <section class="intro">
    <h2 class="intro-heading">Consulting</h2>
    <p class="intro-text">We’re known for our pragmatism, in depth analysis, strategic insight and nurturing long-term client self-sufficiency. We approach business consulting differently, with a Genuine Client focus.</p>
  </section>
</div>
</body>
</html>
```